Business card design needed

I need a business card for my new Food & Lifestyle Coaching business - "Bloomwell Food & Lifestlye Coaching"

i already have a logo and would like to have that incorporated into the business card, obviously.

i would like a design that says "fresh" and "funky" - my target market is female, aged 20-45 so i want something that will stand out to them when they see it.

My "Company Colour" is Apple Green
Updates

Thankyou to everyone who has submitted a design for my project. At this stage i have quite a large number of designs to chose from and with only a short time until my project closes i am focusing now on chosing from those i have already shortlisted so am unfortunately not considering any new desings.

Thankyou again for your interest in my project.

Target Market(s)

Female, Health Conscious (or looking to improve their health/lifestyle), aged between 20-45

Industry/Entity Type

Business

Contact Information for Business Card

Tessa Harlow
Ph: 0438215790
Email: hellobloom@quarlmail.com

Requirements
Must have
• Must include my existing Logo
Nice to have
• Would be nice to incoirporate and appointment card on the back

```html
<!DOCTYPE html>
<html lang="en">
<head>
<meta charset="utf-8">
<title>Bloomwell Business Card</title>
<link rel="stylesheet" href="https://fonts.googleapis.com/css2?family=Arimo:wght@400;700&display=swap">
<style>
  :root {
    --apple-green: #8cc63f;
    --ink: #1a1a1a;
    --muted: #555555;
    --rule: #777777;
    --paper: #ffffff;
    --backdrop: #2a2a2a;
  }
  * { box-sizing: border-box; margin: 0; padding: 0; }
  html, body {
    width: 1200px; height: 900px; overflow: hidden;
    background: var(--backdrop);
    font-family: "Arimo", Arial, sans-serif;
  }
  .canvas { position: relative; width: 1200px; height: 900px; }
  .card {
    position: absolute; width: 540px; height: 308px;
    background: var(--paper);
    box-shadow: 0 12px 30px rgba(0,0,0,.45);
  }
  .card--back { left: 90px; top: 90px; }
  .card--front { left: 570px; top: 500px; }

  .brand { display: flex; align-items: center; gap: 8px; }
  .brand__dot { width: 18px; height: 18px; border-radius: 50%; background: var(--apple-green); }
  .brand__name { font-size: 30px; font-weight: 400; color: var(--apple-green); letter-spacing: .5px; }
  .brand__tagline { font-size: 10px; color: var(--muted); }

  /* appointment side */
  .card--back .brand { position: absolute; left: 150px; top: 38px; }
  .card--back .brand__tagline { position: absolute; left: 176px; top: 80px; }
  .appt { position: absolute; left: 50px; right: 50px; top: 112px; }
  .appt__row { display: flex; gap: 24px; margin-bottom: 26px; }
  .appt__field { flex: 1; border-bottom: 1px solid var(--rule); height: 22px; position: relative; }
  .appt__spacer { flex: 1; }
  .appt__field--short { flex: .5; }
  .appt__label { position: absolute; font-size: 9px; color: var(--muted); top: 25px; white-space: nowrap; }
  .appt__label--right { right: 0; }
  .appt__label--left { left: 0; }
  .appt__label--center { left: 50%; transform: translateX(-50%); }
  .appt__phone {
    position: absolute; left: 0; right: 0; bottom: 24px; text-align: center;
    font-size: 13px; letter-spacing: 10px; color: var(--ink);
  }

  /* contact side */
  .mark {
    position: absolute; left: 45px; top: 80px;
    width: 150px; height: 150px; border-radius: 50%;
    background: var(--apple-green);
  }
  .card--front .brand { position: absolute; right: 40px; top: 26px; }
  .card--front .brand__tagline { position: absolute; right: 40px; top: 68px; }
  .contact { position: absolute; right: 40px; top: 100px; text-align: right; }
  .contact__name { font-size: 26px; font-weight: 700; color: var(--ink); letter-spacing: -.5px; }
  .contact__name-last { color: var(--apple-green); }
  .contact__phone { font-size: 15px; color: var(--ink); margin-top: 2px; padding-bottom: 6px;
    border-bottom: 2px dotted var(--apple-green); }
  .contact__email { font-size: 15px; color: var(--apple-green); margin-top: 8px; }
  .contact__email-domain { color: var(--ink); }
</style>
</head>
<body>
<main class="canvas">

  <section class="card card--back" aria-label="Appointment card">
    <div class="brand">
      <span class="brand__dot"></span>
      <span class="brand__name">Bloomwell</span>
    </div>
    <p class="brand__tagline">Food &amp; Lifestlye Coaching</p>

    <div class="appt">
      <div class="appt__row">
        <div class="appt__field"><span class="appt__label appt__label--center">has an appointment on</span></div>
      </div>
      <div class="appt__row">
        <div class="appt__field"><span class="appt__label appt__label--left">day</span></div>
        <div class="appt__field"><span class="appt__label appt__label--center">month</span></div>
        <div class="appt__field"><span class="appt__label appt__label--right">date</span></div>
      </div>
      <div class="appt__row">
        <div class="appt__field appt__field--short"><span class="appt__label appt__label--center">time</span></div>
        <div class="appt__spacer"></div>
      </div>
    </div>
    <p class="appt__phone">0438 215 790</p>
  </section>

  <section class="card card--front" aria-label="Business card">
    <div class="mark"></div>

    <div class="brand">
      <span class="brand__dot"></span>
      <span class="brand__name">Bloomwell</span>
    </div>
    <p class="brand__tagline">Food &amp; Lifestlye Coaching</p>

    <div class="contact">
      <p class="contact__name">tessa<span class="contact__name-last">harlow</span></p>
      <p class="contact__phone">0438 215 790</p>
      <p class="contact__email">hellobloom<span class="contact__email-domain">@quarlmail.com</span></p>
    </div>
  </section>

</main>
</body>
</html>
```